Need a fun and informative infographic!

We need an infographic to describe our "client experience" which consists of 4 phases - see info about each of our "phases" which includes our available suite of services. UPDATED THE TEXT IN A NEW FILE CALLED "Client Experience Infographic Info".

We intend to use the infographic in both print and digital in a printed "leave behind", in packets for new clients, and possible on the website.

Lantern Tutors www.lanterntutors.example

Target Market(s)

Families of children aged Kindergarten through 12th Grade; affluent communities who have expendable income to spend on private tutoring and test prep.

Industry/Entity Type

Education

Font styles to use
Sans Serif

Requirements
Must have
• My project must use our brand colors.
• Light Blue CMYK: 60 27 0 0 RGB: 115 165 215
• Dark Blue CMYK: 93 85 36 27 RGB: 43 57 94
• Orange CMYK: 0 46 77 10 RGB: 230 125 53

```html
<!DOCTYPE html>
<html lang="en">
<head>
<meta charset="utf-8">
<title>Lantern Tutors — Client Experience</title>
<link rel="stylesheet" href="https://fonts.googleapis.com/css2?family=Anton&family=Arimo:wght@400;700&display=swap">
<style>
  :root{
    --navy:#2b395e;
    --light-blue:#73a5d7;
    --orange:#e67d35;
    --yellow:#e9ac25;
    --charcoal:#2e2e30;
    --charcoal-mid:#363638;
    --charcoal-deep:#1f1f21;
    --white:#ffffff;
    --divider:rgba(255,255,255,.55);
  }
  *{box-sizing:border-box;margin:0;padding:0}
  html,body{width:1200px;height:1200px;overflow:hidden;background:var(--white)}
  .stage{position:absolute;left:0;top:0;width:1500px;height:1500px;transform:scale(.8);transform-origin:0 0}
  .backdrop{position:absolute;left:0;top:0}
  .brand{position:absolute;left:500px;top:92px;width:450px;text-align:center}
  .brand-name{font-family:"Arimo",sans-serif;font-weight:700;font-size:52px;color:var(--navy);letter-spacing:-.5px;line-height:1}
  .brand-tagline{font-family:"Arimo",sans-serif;font-size:21px;color:var(--navy);letter-spacing:2px;margin-top:16px}
  .badge{position:absolute;width:212px;height:162px}
  .badge-back{position:absolute;left:0;top:6px;width:212px;height:150px;background:var(--yellow)}
  .badge-front{position:absolute;left:30px;top:0;width:153px;height:162px;background:var(--orange);box-shadow:0 3px 6px rgba(0,0,0,.35);
    display:flex;flex-direction:column;align-items:center;justify-content:center;font-family:"Anton",sans-serif;color:var(--white);line-height:1}
  .badge-label{font-size:48px;letter-spacing:.5px}
  .badge-number{font-size:58px;margin-top:6px}
  .phase-title{position:absolute;font-family:"Anton",sans-serif;font-weight:400;font-size:37px;color:var(--white);line-height:1.18;letter-spacing:0}
  .phase-copy{position:absolute;font-family:"Arimo",sans-serif;font-weight:700;font-size:16.5px;line-height:20.4px;color:var(--white);text-transform:uppercase;letter-spacing:.3px}
  .phase-copy ul{list-style:none}
  .phase-copy li::before{content:".\00a0\00a0"}
</style>
</head>
<body>
<div class="stage">
  <svg class="backdrop" width="1500" height="1500" viewBox="0 0 1500 1500" xmlns="http://www.w3.org/2000/svg">
    <rect x="173" y="10" width="1140" height="1475" fill="var(--charcoal)"/>
    <path d="M440 95 C470 40 560 28 640 30 L820 30 C900 28 990 40 1010 95 C1030 110 1050 118 1068 128 C1050 140 1030 148 1010 165 C990 215 900 230 820 228 L640 228 C560 230 470 215 440 165 C420 148 400 140 385 128 C400 118 420 110 440 95 Z" fill="var(--white)" stroke="#d8d8d8" stroke-width="2"/>
    <polygon points="173,258 455,258 470,272 173,272" fill="var(--orange)"/>
    <polygon points="455,258 703,258 715,272 470,272" fill="var(--yellow)"/>
    <polygon points="703,258 970,258 985,272 715,272" fill="var(--navy)"/>
    <polygon points="970,258 1235,258 1245,272 985,272" fill="var(--orange)"/>
    <rect x="173" y="272" width="1140" height="134" fill="var(--charcoal-mid)"/>
    <g stroke="#4a4a4d" stroke-width="2">
      <line x1="255" y1="292" x2="255" y2="395"/><line x1="477" y1="292" x2="477" y2="395"/>
      <line x1="503" y1="292" x2="503" y2="395"/><line x1="727" y1="292" x2="727" y2="395"/>
      <line x1="753" y1="292" x2="753" y2="395"/><line x1="975" y1="292" x2="975" y2="395"/>
      <line x1="1003" y1="292" x2="1003" y2="395"/><line x1="1225" y1="292" x2="1225" y2="395"/>
    </g>
    <g fill="none" stroke="var(--white)" stroke-width="3" stroke-linecap="round" stroke-linejoin="round">
      <rect x="315" y="308" width="95" height="64" rx="6"/>
      <line x1="342" y1="384" x2="382" y2="384"/>
      <polyline points="333,355 348,340 360,350 375,330 385,340 395,322"/>
      <path d="M845 308 L885 308 L898 322 L898 385 L833 385 L833 320 Z"/>
      <line x1="845" y1="340" x2="880" y2="340"/><line x1="845" y1="355" x2="872" y2="355"/><line x1="845" y1="370" x2="868" y2="370"/>
      <path d="M875 375 L908 330 L918 338 L885 383 L872 386 Z"/>
    </g>
    <rect x="580" y="308" width="72" height="80" rx="10" fill="#4a4a4d" role="img" aria-label="Icon: tutor figure"/>
    <rect x="1072" y="308" width="88" height="78" rx="6" fill="#4a4a4d" role="img" aria-label="Icon: teacher at a presentation board"/>

    <rect x="1150" y="408" width="163" height="124" fill="var(--charcoal-mid)"/>
    <rect x="1150" y="532" width="163" height="118" fill="var(--charcoal-deep)"/>
    <polygon points="173,408 1200,408 1150,532 1200,650 173,650" fill="var(--navy)"/>

    <rect x="173" y="660" width="160" height="122" fill="var(--charcoal-mid)"/>
    <rect x="173" y="782" width="160" height="120" fill="var(--charcoal-deep)"/>
    <polygon points="280,660 1313,660 1313,902 280,902 330,782" fill="var(--navy)"/>

    <rect x="1150" y="918" width="163" height="128" fill="var(--charcoal-mid)"/>
    <rect x="1150" y="1046" width="163" height="116" fill="var(--charcoal-deep)"/>
    <polygon points="173,918 1200,918 1150,1046 1200,1162 173,1162" fill="var(--navy)"/>

    <rect x="173" y="1178" width="160" height="142" fill="var(--charcoal-mid)"/>
    <rect x="173" y="1320" width="160" height="137" fill="var(--charcoal-deep)"/>
    <polygon points="282,1178 1313,1178 1313,1457 282,1457 334,1320" fill="var(--navy)"/>

    <g stroke="var(--divider)" stroke-width="1.5" stroke-dasharray="2 2">
      <line x1="785" y1="414" x2="785" y2="645"/>
      <line x1="685" y1="666" x2="685" y2="897"/>
      <line x1="795" y1="924" x2="795" y2="1157"/>
      <line x1="671" y1="1184" x2="671" y2="1450"/>
      <line x1="1042" y1="1184" x2="1042" y2="1450"/>
    </g>
  </svg>

  <header class="brand">
    <div class="brand-name">Lantern Tutors</div>
    <div class="brand-tagline">Bright minds, steady steps.</div>
  </header>

  <!-- Phase 01 -->
  <div class="badge" style="left:202px;top:447px"><div class="badge-back"></div><div class="badge-front"><span class="badge-label">PHASE</span><span class="badge-number">01</span></div></div>
  <h2 class="phase-title" style="left:428px;top:478px">The Consultation</h2>
  <p class="phase-copy" style="left:428px;top:527px;width:330px">The process begins with a complimentary and thorough consultation.</p>
  <p class="phase-copy" style="left:804px;top:478px;width:340px">One of our local educational directors meets in-person<br>(or via LinkCall if necessary)<br>with the<br>parents and student to become aquinted and to better understand the family’s needs.</p>

  <!-- Phase 02 -->
  <h2 class="phase-title" style="left:343px;top:694px">Match and Customize</h2>
  <p class="phase-copy" style="left:341px;top:747px;width:335px">Students are matched with a tutor or a team of tutors based on a careful understanding of each student’s unique learning style, academic goals, personality and schedule</p>
  <p class="phase-copy" style="left:701px;top:722px;width:352px">The tutor(s) develop a<br>personalized curriculum that aligns with the student’s existing strengths and areas for improvement, while addressing all factors impacting performance such as test anxiety and self-confidence.</p>
  <div class="badge" style="left:1086px;top:702px"><div class="badge-back"></div><div class="badge-front"><span class="badge-label">PHASE</span><span class="badge-number">02</span></div></div>

  <!-- Phase 03 -->
  <div class="badge" style="left:202px;top:967px"><div class="badge-back"></div><div class="badge-front"><span class="badge-label">PHASE</span><span class="badge-number">03</span></div></div>
  <h2 class="phase-title" style="left:440px;top:958px">Communication</h2>
  <p class="phase-copy" style="left:436px;top:1009px;width:352px">Tutoring sessions occur in the home, our offices, remotely, or at a location of the family’s choosing; scheduling is based on the availability of the student and tutor.</p>
  <p class="phase-copy" style="left:803px;top:1002px;width:345px">Our custom-built, mobile-friendly “dashboard” provides parents with a thorough lesson summary after each session, convenient practice test registration, and real-time tracking of student progress.</p>

  <!-- Phase 04 -->
  <h2 class="phase-title" style="left:330px;top:1206px;width:300px;text-align:center">Ongoing Suite of<br>Services</h2>
  <p class="phase-copy" style="left:346px;top:1304px;width:320px">Our educational directors are compassionate and responsive, ready to provide guidance and seamless coordination of whatever services the student requires.</p>
  <div class="phase-copy" style="left:685px;top:1187px;width:345px">
    <p>No matter where along the path<br>our relationship begins, we<br>continue to support our<br>students and families in a myriad<br>of ways including:</p>
    <ul><li>Standardized test prep</li><li>Subject tutoring</li><li>College admissions consulting</li></ul>
    <p>When appropriate, we introduce behaviors for students to improve their executive function&shy;ing, organizational and time man&shy;agement.</p>
  </div>
  <div class="badge" style="left:1075px;top:1235px"><div class="badge-back"></div><div class="badge-front"><span class="badge-label">PHASE</span><span class="badge-number">04</span></div></div>
</div>
</body>
</html>
```